Lanterns for Paws Christmas Cards

We want to send this to all our donors and partners. Hoping for a design that says hope and compassion and shows the benefit of their support. We offer essential pet programs to the vulnerable such as a pet food bank. safekeeping, youth and senior education, vet care assistance. Thank you!

```html
<!DOCTYPE html>
<html lang="en">
<head>
<meta charset="utf-8">
<title>Lanterns for Paws Christmas Card</title>
<link href="https://fonts.googleapis.com/css2?family=Montserrat:wght@500;800&family=Comfortaa:wght@400&family=Jost:wght@400&display=swap" rel="stylesheet">
<style>
:root{
  --bg:#bebdbe;
  --red:#d71920;
  --red-dark:#9c1419;
  --red-mid:#c4161d;
  --white:#ffffff;
  --paper:#f3f3f3;
  --paper-shade:#dcdcdc;
  --ink:#2a2a2a;
  --photo-a:#8a7a6c;
  --photo-b:#c9b8a4;
}
*{box-sizing:border-box;margin:0;padding:0}
html,body{width:982px;height:1200px;overflow:hidden;background:var(--bg)}
.canvas{position:relative;width:982px;height:1200px}
.spread{position:absolute;left:31px;width:920px;height:550px;display:flex;box-shadow:0 10px 24px rgba(0,0,0,.25)}
.spread--outer{top:30px}
.spread--inner{top:620px}
.page{position:relative;width:460px;height:550px;overflow:hidden}
.page--back{background:linear-gradient(100deg,var(--red-dark) 0%,var(--red) 35%,var(--red-mid) 70%,var(--red-dark) 100%);color:var(--white)}
.page--front{background:linear-gradient(180deg,var(--white),#eeeeee)}
.page--inside-left{background:linear-gradient(90deg,var(--paper),var(--paper-shade))}
.page--inside-right{background:linear-gradient(90deg,var(--paper-shade),var(--paper) 30%,var(--white))}
.brand{position:absolute;left:0;right:0;text-align:center}
.brand__mark{width:86px;height:86px;border-radius:50%;margin:0 auto 18px}
.brand__name{font-family:"Montserrat",sans-serif;font-weight:800;font-size:34px;letter-spacing:.5px;line-height:1.05}
.brand__tagline{margin-top:14px;font-family:"Comfortaa",sans-serif;font-size:13px;letter-spacing:.5px}
.page--back .brand{top:150px}
.page--back .brand__mark{border:3px solid var(--white)}
.page--front .brand{top:235px;color:var(--red)}
.page--front .brand__mark{background:var(--red);width:80px;height:80px}
.page--front .brand__tagline{color:var(--ink)}
.social{position:absolute;top:430px;left:0;right:0;display:flex;justify-content:center;gap:10px}
.social span{width:20px;height:20px;border-radius:50%;background:var(--white)}
.website{position:absolute;top:462px;left:0;right:0;text-align:center;font-family:"Comfortaa",sans-serif;font-size:14px;letter-spacing:.5px}
.wave{position:absolute;top:0;left:0;width:460px;height:200px}
.tree{position:absolute;left:165px;top:40px;width:130px;height:140px;border-radius:50% 50% 8px 8px;background:radial-gradient(circle at 50% 12%,#ffcf4a 0 8%,var(--red) 30%,var(--red-dark))}
.frame{position:absolute;inset:28px;border:1.5px solid var(--red-dark)}
.snowflake{position:absolute;width:22px;height:22px;border-radius:50%;background:var(--red)}
.sf-tl{left:17px;top:17px}.sf-tr{right:17px;top:17px}.sf-bl{left:17px;bottom:17px}.sf-br{right:17px;bottom:17px}
.inner-brand{position:absolute;left:0;right:0;text-align:center;color:var(--red)}
.inner-brand__mark{width:56px;height:56px;border-radius:50%;background:var(--red);margin:0 auto 10px}
.inner-brand__name{font-family:"Montserrat",sans-serif;font-weight:800;font-size:22px}
.page--inside-left .inner-brand{top:150px}
.page--inside-right .inner-brand{top:70px}
.headline{position:absolute;left:50px;right:50px;text-align:center;font-family:"Montserrat",sans-serif;font-weight:800;color:var(--red);font-size:13.5px;line-height:1.3}
.page--inside-left .headline{top:262px}
.page--inside-right .headline{top:175px}
.body-copy{position:absolute;left:52px;right:52px;top:312px;text-align:center;font-family:"Jost",sans-serif;font-size:11px;line-height:1.55;color:var(--ink)}
.photos{position:absolute;left:60px;right:40px;top:262px;display:flex;flex-wrap:wrap;justify-content:center;gap:10px 8px}
.photo{width:64px;height:64px;border-radius:50%;background:radial-gradient(circle at 40% 35%,var(--photo-b),var(--photo-a))}
.photos-row{display:flex;justify-content:center;gap:8px;width:100%}
</style>
</head>
<body>
<main class="canvas">
  <section class="spread spread--outer">
    <article class="page page--back">
      <div class="brand">
        <div class="brand__mark"></div>
        <div class="brand__name">LANTERNS<br>FOR PAWS</div>
        <div class="brand__tagline">Neighbours · Animals · Care</div>
      </div>
      <div class="social"><span></span><span></span><span></span></div>
      <div class="website">www.lanternsforpaws.org</div>
    </article>
    <article class="page page--front">
      <svg class="wave" viewBox="0 0 460 200" aria-hidden="true">
        <defs><linearGradient id="waveRed" x1="0" x2="1"><stop offset="0" stop-color="#9c1419"/><stop offset=".4" stop-color="#d71920"/><stop offset="1" stop-color="#d71920"/></linearGradient></defs>
        <path d="M0 0H460V120C380 130 300 170 230 175C150 180 70 160 0 165Z" fill="url(#waveRed)"/>
      </svg>
      <div class="tree" role="img" aria-label="Christmas tree drawn as a red ribbon with a glowing star on top"></div>
      <div class="brand">
        <div class="brand__mark"></div>
        <div class="brand__name">LANTERNS<br>FOR PAWS</div>
        <div class="brand__tagline">Neighbours · Animals · Care</div>
      </div>
    </article>
  </section>

  <section class="spread spread--inner">
    <article class="page page--inside-left">
      <div class="frame"></div>
      <span class="snowflake sf-tl" role="img" aria-label="Red snowflake ornament"></span>
      <span class="snowflake sf-tr" role="img" aria-label="Red snowflake ornament"></span>
      <span class="snowflake sf-bl" role="img" aria-label="Red snowflake ornament"></span>
      <span class="snowflake sf-br" role="img" aria-label="Red snowflake ornament"></span>
      <div class="inner-brand">
        <div class="inner-brand__mark"></div>
        <div class="inner-brand__name">Lanterns for Paws</div>
      </div>
      <h2 class="headline">Our priority is helping vulnerable members of our community during times of hardship</h2>
      <p class="body-copy">Our Beacon Team is readily available to help Calgarians in need 24/7. This service is available to Calgarians in emergency situations such as fire, flood or inclement weather. We provide Calgarians the resources to get themselves and their pets to a safe location or intervene when needed.</p>
    </article>
    <article class="page page--inside-right">
      <div class="frame"></div>
      <span class="snowflake sf-tl" role="img" aria-label="Red snowflake ornament"></span>
      <span class="snowflake sf-tr" role="img" aria-label="Red snowflake ornament"></span>
      <span class="snowflake sf-bl" role="img" aria-label="Red snowflake ornament"></span>
      <span class="snowflake sf-br" role="img" aria-label="Red snowflake ornament"></span>
      <div class="inner-brand">
        <div class="inner-brand__mark"></div>
        <div class="inner-brand__name">Lanterns for Paws</div>
      </div>
      <h2 class="headline">We are dedicated to honouring the importance of the human-animal bond by helping vulnerable Calgarians with their pets before they turn to shelters.</h2>
      <div class="photos">
        <div class="photos-row">
          <div class="photo" role="img" aria-label="Photo of a small fluffy dog with donated supplies"></div>
          <div class="photo" role="img" aria-label="Photo of a person hugging their dog outdoors"></div>
          <div class="photo" role="img" aria-label="Photo of a puppy beside a bowl of food"></div>
          <div class="photo" role="img" aria-label="Photo of two happy dogs at home"></div>
        </div>
        <div class="photos-row">
          <div class="photo" role="img" aria-label="Photo of a black puppy on a plaid blanket"></div>
          <div class="photo" role="img" aria-label="Photo of a person cuddling a dog"></div>
        </div>
      </div>
    </article>
  </section>
</main>
</body>
</html>
```